Tallyleaf Web Design

Create Website Design for Tallyleaf. Tallyleaf is online application for collaboration team work system (task list management). More concept design for this project please find attach file ("tallyleaf website concept.pdf") . But my concept is just describe minimal features not bind design

For tallyleaf logo, i had already attach files. But i had not decided what color i chose, so it's okay if you suggest logo color for your suitable website design.
Updates

Dear All Designer,

I like brisk carousel (http://quorvanlabs.example/brisk-carousel/),
may be your concept design can adjust with this concept.
but don't worry about script for brisk carousel, my team will be handle
You just make website design to suitable with brisk carousel

but if you had own website design concept are welcome

thanks

Target Market(s)

Business Company

Industry/Entity Type

Management

```html
<!DOCTYPE html>
<html lang="en">
<head>
<meta charset="utf-8">
<title>Tallyleaf — Online Collaboration Team Work</title>
<link href="https://fonts.googleapis.com/css2?family=Source+Sans+3:wght@400;600&family=PT+Sans+Narrow:wght@700&display=swap" rel="stylesheet">
<style>
:root{
  --brand:#2b8fb8;
  --brand-dot:#9a5cb0;
  --nav-text:#4a4a4a;
  --divider:#c9c9c9;
  --orange:#f7901e;
  --orange-dark:#ef7a06;
  --purple:#8e55a4;
  --blue:#1d6f9f;
  --hero-top:#80cde2;
  --hero-bottom:#22a0c4;
  --hero-ink:#0d5674;
  --hero-body:#1f5f78;
  --dot:#136d93;
  --dot-active:#8fd6ea;
  --card-border:#dcdcdc;
  --body-text:#5a5a5a;
  --footer-bg:#2d2d2d;
  --footer-text:#cfcfcf;
  --white:#ffffff;
}
*{box-sizing:border-box;margin:0;padding:0}
html,body{width:1200px;height:1114px;overflow:hidden;background:var(--white)}
body{position:relative;font-family:"Source Sans 3",Arial,sans-serif;color:var(--body-text)}

.site-header{position:absolute;left:0;top:0;width:1200px;height:125px;background:var(--white)}
.brand{position:absolute;left:70px;top:38px;display:flex;align-items:center;gap:10px}
.brand-name{font-size:54px;font-weight:600;color:var(--brand);letter-spacing:-1px;line-height:1}
.brand-mark{width:22px;height:22px;border-radius:50%;background:var(--brand-dot)}
.main-nav{position:absolute;left:550px;top:64px;display:flex;align-items:center}
.main-nav a{font-size:19px;color:var(--nav-text);text-decoration:none;padding:0 17px;border-left:1px solid var(--divider);line-height:22px}
.main-nav a:first-child{border-left:0;padding-left:0}
.login-btn{position:absolute;left:1027px;top:55px;width:95px;height:39px;border-radius:4px;background:linear-gradient(var(--orange),var(--orange-dark));color:var(--white);font-size:18px;text-align:center;line-height:38px;text-decoration:none}

.hero{position:absolute;left:0;top:125px;width:1200px;height:449px;background:linear-gradient(var(--hero-top),var(--hero-bottom));border-top:1px dashed #9ad7e8}
.hero-frame{position:absolute;left:72px;top:35px;width:548px;height:363px;background:var(--white);padding:8px;box-shadow:0 8px 14px rgba(0,60,90,.25)}
.hero-photo{width:100%;height:100%;background:linear-gradient(160deg,#dfe8ef 0%,#b9c9d6 45%,#38404a 100%);position:relative}
.play-btn{position:absolute;left:50%;top:47%;transform:translate(-50%,-50%)}
.hero-copy{position:absolute;left:684px;top:80px;width:480px}
.hero-title{font-size:41px;font-weight:400;color:var(--white);line-height:45px}
.hero-lead{margin-top:10px;font-size:20px;font-weight:600;color:var(--hero-ink)}
.hero-text{margin-top:8px;font-size:14px;line-height:21px;color:var(--hero-body);width:440px}
.learn-btn{display:inline-block;margin-top:14px;width:110px;height:33px;background:var(--hero-ink);color:var(--white);font-family:"PT Sans Narrow",Arial,sans-serif;font-size:15px;text-align:center;line-height:33px;border-radius:2px}
.carousel-dots{position:absolute;left:691px;top:354px;display:flex;gap:5px}
.carousel-dots span{width:11px;height:11px;border-radius:50%;background:var(--dot)}
.carousel-dots span.is-active{background:var(--dot-active)}

.features{position:absolute;left:0;top:617px;width:1200px}
.feature-card{position:absolute;top:0;width:350px;height:330px;background:var(--white);border:1px solid var(--card-border);box-shadow:0 12px 10px -8px rgba(0,0,0,.12)}
.feature-card:nth-child(1){left:49px}
.feature-card:nth-child(2){left:419px}
.feature-card:nth-child(3){left:789px}
.feature-title{height:56px;color:var(--white);font-size:23px;font-weight:400;text-align:center;line-height:56px}
.feature-card--orange .feature-title{background:var(--orange)}
.feature-card--purple .feature-title{background:var(--purple)}
.feature-card--blue .feature-title{background:var(--blue)}
.feature-media{margin:14px auto 0;width:315px;height:141px;border:1px solid #e2e2e2}
.media-app{background:linear-gradient(#dde9f7,#f4f7fb)}
.media-sync{background:linear-gradient(#f6f8fb,#9ec3e6)}
.media-report{background:linear-gradient(135deg,#f2f2f2,#d7dde6 60%,#7fb3dd)}
.feature-text{margin:20px 0 0 27px;width:300px;font-size:14px;line-height:23px;color:var(--body-text)}

.site-footer{position:absolute;left:0;top:1016px;width:1200px;height:98px;background:var(--footer-bg)}
.copyright{position:absolute;left:58px;top:35px;font-size:13px;color:var(--footer-text)}
.footer-nav{position:absolute;left:668px;top:35px;display:flex}
.footer-nav a{font-size:14px;font-weight:600;color:var(--white);text-decoration:none;padding:0 12px;border-left:1px solid #bbb;line-height:16px}
.footer-nav a:first-child{border-left:0;padding-left:0}
.social{position:absolute;left:1042px;top:32px;display:flex;gap:8px}
.social span{width:22px;height:22px;border-radius:50%;background:var(--white)}
</style>
</head>
<body>
<header class="site-header">
  <div class="brand"><span class="brand-name">tallyleaf</span><span class="brand-mark"></span></div>
  <nav class="main-nav">
    <a href="#">Main</a><a href="#">About Us</a><a href="#">Process</a><a href="#">Project</a><a href="#">Contact</a>
  </nav>
  <a class="login-btn" href="#">Log In</a>
</header>

<section class="hero">
  <div class="hero-frame">
    <div class="hero-photo" role="img" aria-label="Photo of a team of three colleagues working together at a laptop">
      <svg class="play-btn" width="58" height="58" viewBox="0 0 58 58" aria-hidden="true">
        <circle cx="29" cy="29" r="27" fill="#ffffff"/>
        <circle cx="29" cy="29" r="23" fill="#222"/>
        <path d="M24 19 L38 29 L24 39 Z" fill="#ffffff"/>
      </svg>
    </div>
  </div>
  <div class="hero-copy">
    <h1 class="hero-title">Customize Online Collaboration Team Work</h1>
    <p class="hero-lead">Lorem ipsum dolor sit amet adipiscing elit.</p>
    <p class="hero-text">Aliquam vehicula mi at mauris. Maecenas placerat, nisl at consequat rhoncus, sem nunc gravida justo, quis eleifend arcu velit quis lacus. Morbi magna magna, tincidunt</p>
    <span class="learn-btn">LEARN MORE</span>
  </div>
  <div class="carousel-dots"><span class="is-active"></span><span></span><span></span><span></span></div>
</section>

<section class="features">
  <article class="feature-card feature-card--orange">
    <h2 class="feature-title">Customize Application</h2>
    <div class="feature-media media-app" role="img" aria-label="Screenshot of a code comparison application window"></div>
    <p class="feature-text">Duis tincidunt lectus quis dui viverra vestibulum. Suspendisse vulputate aliquam dui. Nulladui ut augue. Aliquam vehicula mi at mauris.</p>
  </article>
  <article class="feature-card feature-card--purple">
    <h2 class="feature-title">Synchronize All Device</h2>
    <div class="feature-media media-sync" role="img" aria-label="Illustration of groups of people connected to a central server"></div>
    <p class="feature-text">Duis tincidunt lectus quis dui viverra vestibulum. Suspendisse vulputate aliquam dui. Nulladui ut augue. Aliquam vehicula mi at mauris.</p>
  </article>
  <article class="feature-card feature-card--blue">
    <h2 class="feature-title">Report</h2>
    <div class="feature-media media-report" role="img" aria-label="Photo of printed report charts with a pen"></div>
    <p class="feature-text">Duis tincidunt lectus quis dui viverra vestibulum. Suspendisse vulputate aliquam dui. Nulladui ut augue. Aliquam vehicula mi at mauris.</p>
  </article>
</section>

<footer class="site-footer">
  <p class="copyright">Copyright © 2012 Company Name.&nbsp; All right reserved.&nbsp; Term of Use</p>
  <nav class="footer-nav">
    <a href="#">Main</a><a href="#">About Us</a><a href="#">Process</a><a href="#">Project</a><a href="#">Contact</a>
  </nav>
  <div class="social" aria-label="Social links"><span></span><span></span><span></span></div>
</footer>
</body>
</html>
```